M Website

We need a website design for a construction plant company. You may use a combination of our photos and the stock images. See the logo for company colours. It also be of great value to see moving pictures like the ones on the link: https://www.quindellworks.co.za/copy-of-about-us. See our uploaded files for content.

Target Market(s)

Construction

Number of Pages Required

5+ page

```html
<!DOCTYPE html>
<html lang="en">
<head>
<meta charset="utf-8">
<title>Kestrel Logistics and Plant Hire</title>
<link href="https://fonts.googleapis.com/css2?family=Montserrat:wght@300;400;500;600&display=swap" rel="stylesheet">
<style>
:root{
  --yellow:#f5c400;
  --dark:#232323;
  --darker:#1a1a1a;
  --ink:#2b2b2b;
  --muted:#777;
  --light:#ffffff;
  --field:#5a5a5a;
  --line:#e6e6e6;
}
*{margin:0;padding:0;box-sizing:border-box}
html,body{width:1200px;height:4369px;overflow:hidden}
body{font-family:'Montserrat',sans-serif;color:var(--ink);background:var(--light);position:relative}
.abs{position:absolute}
.btn{position:absolute;border:2px solid var(--yellow);color:var(--yellow);font-size:15px;letter-spacing:1px;display:flex;align-items:center;justify-content:center;text-transform:uppercase;background:transparent}
.btn.dark-text{color:var(--yellow)}

/* hero */
.hero{left:0;top:0;width:1200px;height:612px;background:linear-gradient(160deg,#5d6770 0%,#3b4148 45%,#2a2c2f 100%)}
.hero-shade{left:0;top:0;width:1200px;height:117px;background:rgba(20,20,20,.55)}
.brand{left:87px;top:22px;display:flex;align-items:center;gap:12px;color:var(--yellow);font-weight:600;font-size:30px;letter-spacing:1px}
.brand .dot{width:34px;height:34px;background:var(--yellow);border-radius:50%}
.topbar{right:87px;top:18px;display:flex;align-items:center;gap:22px;color:var(--yellow);font-size:13px}
.topbar .social{display:flex;gap:14px}
.topbar .social span{width:10px;height:10px;border-radius:50%;background:#ddd}
.nav{right:87px;top:62px;display:flex;font-size:13px;color:#eee;text-transform:uppercase;letter-spacing:.5px}
.nav a{padding:0 11px;border-right:1px solid #999;color:inherit;text-decoration:none}
.nav a:last-child{border-right:none;padding-right:0}
.nav a.active{color:var(--yellow)}
.hero-title{left:0;top:238px;width:1200px;text-align:center;color:#fff;font-weight:300;font-size:58px;line-height:63px;letter-spacing:2px;text-transform:uppercase}

/* intro + projects */
.intro{left:87px;top:668px;width:1026px;font-size:14px;line-height:24px;color:#444}
.project{position:absolute;width:326px;height:282px}
.project .photo{position:absolute;left:0;top:0;width:326px;height:282px}
.project .label{position:absolute;left:24px;bottom:-3px;width:278px;height:58px;background:var(--yellow);color:#fff;text-align:center;padding-top:10px}
.project .label b{display:block;font-weight:500;font-size:15px;letter-spacing:1px}
.project .label small{display:block;font-size:11px;color:#333;margin-top:4px}

/* services */
.services{left:0;top:1503px;width:1200px;height:717px;background:var(--dark)}
.section-title{position:absolute;left:0;width:1200px;text-align:center;font-size:42px;font-weight:400;letter-spacing:1px;text-transform:uppercase}
.section-sub{position:absolute;left:0;width:1200px;text-align:center;font-size:14px}
.underline{position:absolute;left:580px;width:40px;height:2px;background:var(--yellow)}
.service{position:absolute;top:233px;width:236px}
.service .photo{width:236px;height:236px}
.service .bar{width:40px;height:2px;background:var(--yellow);margin:21px auto 0}
.service p{color:#eee;text-align:center;font-size:15px;line-height:21px;margin-top:16px;text-transform:uppercase}

/* why */
.why-card{position:absolute;width:326px;height:270px;background:#fff;box-shadow:0 0 12px rgba(0,0,0,.12);text-align:center}
.why-card.featured{background:var(--yellow)}
.why-card .icon{width:84px;height:84px;border-radius:50%;border:1px solid #eee;margin:34px auto 0;display:flex;align-items:center;justify-content:center;background:#fff}
.why-card.featured .icon{background:transparent;border-color:rgba(255,255,255,.5)}
.why-card h3{font-weight:400;font-size:18px;margin-top:30px;text-transform:uppercase;letter-spacing:.5px}
.why-card p{font-size:13px;line-height:24px;color:var(--muted);margin:8px auto 0;width:240px}
.why-card.featured p{color:#333}

/* video */
.video-band{left:0;top:3053px;width:1200px;height:268px;background:var(--dark)}
.video{left:87px;top:3274px;width:1026px;height:414px;background:linear-gradient(180deg,#8aa3bf 0%,#b59a6e 55%,#7a6448 100%);box-shadow:0 6px 18px rgba(0,0,0,.3)}
.video-caption{left:122px;top:3630px;border-left:3px solid var(--yellow);padding-left:14px;color:#fff}
.video-caption b{display:block;font-size:14px;font-weight:500;letter-spacing:.5px}
.video-caption span{font-size:12px}

/* contact */
.map{left:150px;top:3700px;width:900px;height:480px;background:radial-gradient(ellipse at center,#eeeeee 0%,#fafafa 60%,#fff 100%)}
.field{position:absolute;background:var(--field);color:#eee;font-size:12px;letter-spacing:1px;display:flex;align-items:flex-start;padding:12px 16px;gap:10px;text-transform:uppercase}
.field svg{flex:none}

/* footer */
.footer{left:0;top:4244px;width:1200px;height:125px;background:var(--darker)}
.footer .brand{top:44px;font-size:24px}
.footer .brand .dot{width:26px;height:26px}
.footer-links{left:325px;top:54px;display:flex;font-size:12px;color:#ddd}
.footer-links span{padding:0 8px;border-right:1px solid #777}
.footer-links span:last-child{border-right:none}
.copy{right:87px;top:54px;font-size:12px;color:#bbb}
</style>
</head>
<body>

<!-- hero -->
<div class="abs hero" role="img" aria-label="Road workers in high-visibility clothing spreading fresh asphalt"></div>
<div class="abs hero-shade"></div>
<div class="abs brand"><span class="dot"></span>KESTREL</div>
<div class="abs topbar">
  <span>
    <svg width="10" height="14" viewBox="0 0 10 14"><rect x="1" y="0.5" width="8" height="13" rx="1.5" fill="none" stroke="#f5c400"/><circle cx="5" cy="11" r="0.9" fill="#f5c400"/></svg>
    +27 (0) 11 555 0142
  </span>
  <span class="social"><span></span><span></span><span></span><span></span></span>
</div>
<nav class="abs nav">
  <a class="active">Home</a><a>Company Overview</a><a>Services</a><a>Personnel</a><a>Experience Record</a><a>Contact Us</a>
</nav>
<h1 class="abs hero-title">Transforming our<br>clients vision into<br>reality</h1>
<div class="btn" style="left:518px;top:443px;width:170px;height:38px">Learn More</div>

<!-- intro -->
<p class="abs intro">Kestrel Logistics and Plant Hire (Pty) Ltd is a Black Woman owned Construction and Plant Hire company operating mainly from the Kestrel head office in Riverbend, Gauteng. Kestrel Logistics and Plant Hire (Pty) Ltd was established in 2014, and has worked in various municipal jurisdictions within South Africa.</p>

<!-- projects -->
<div class="project" style="left:87px;top:752px"><div class="photo" role="img" aria-label="Open highway under blue sky" style="background:linear-gradient(180deg,#3c78c8 0%,#8fbfe8 45%,#5f8d3c 60%,#555 100%)"></div><div class="label"><b>LOREM IPSUM DUMMY</b><small>New York, USA</small></div></div>
<div class="project" style="left:437px;top:752px"><div class="photo" role="img" aria-label="Circular water treatment clarifier" style="background:linear-gradient(180deg,#2f6fb8 0%,#8fc0e0 40%,#9aa7a8 70%,#6c7b7c 100%)"></div><div class="label"><b>LOREM IPSUM DUMMY</b><small>New York, USA</small></div></div>
<div class="project" style="left:789px;top:752px"><div class="photo" role="img" aria-label="Long covered walkway interior" style="background:linear-gradient(180deg,#6c6f73 0%,#c9ccd0 50%,#9a9ca0 100%)"></div><div class="label"><b>LOREM IPSUM DUMMY</b><small>New York, USA</small></div></div>
<div class="project" style="left:87px;top:1081px"><div class="photo" role="img" aria-label="Illuminated bridge at night" style="background:linear-gradient(160deg,#1c2a6e 0%,#6d4cc9 45%,#c26bd6 70%,#233060 100%)"></div><div class="label"><b>LOREM IPSUM DUMMY</b><small>New York, USA</small></div></div>
<div class="project" style="left:437px;top:1081px"><div class="photo" role="img" aria-label="Paved residential road with houses" style="background:linear-gradient(180deg,#8fb3d8 0%,#b6c6a0 40%,#7d8c6a 60%,#8a8a8a 100%)"></div><div class="label"><b>LOREM IPSUM DUMMY</b><small>New York, USA</small></div></div>
<div class="project" style="left:789px;top:1081px"><div class="photo" role="img" aria-label="Curved concrete bridge among trees" style="background:linear-gradient(180deg,#2f4a2a 0%,#6f8d55 50%,#c9c9c0 70%,#3e5a34 100%)"></div><div class="label"><b>LOREM IPSUM DUMMY</b><small>New York, USA</small></div></div>

<div class="btn" style="left:516px;top:1401px;width:172px;height:41px">View More</div>

<!-- services -->
<section class="abs services">
  <h2 class="section-title" style="top:80px;color:#fff">Our Services</h2>
  <div class="underline" style="top:144px"></div>
  <p class="section-sub" style="top:172px;color:#ccc">Lorem Ipsum is simply dummy text of the printing and typesetting industry.</p>
  <div class="service" style="left:87px"><div class="photo" role="img" aria-label="Worker in a trench operating a compactor" style="background:linear-gradient(180deg,#b9c2c6 0%,#8a8e8c 50%,#5d5a55 100%)"></div><div class="bar"></div><p>Road Construction<br>and Rehabilitation</p></div>
  <div class="service" style="left:350px"><div class="photo" role="img" aria-label="Workers in hard hats at an excavation" style="background:linear-gradient(180deg,#9a7a58 0%,#6f5a44 50%,#4a3c2f 100%)"></div><div class="bar"></div><p>Infrastructural<br>Services<br>Development</p></div>
  <div class="service" style="left:615px"><div class="photo" role="img" aria-label="Road roller paving asphalt" style="background:linear-gradient(180deg,#7aa6d8 0%,#a7b68c 40%,#3a3a3a 75%,#222 100%)"></div><div class="bar"></div><p>Water Treatment<br>Works</p></div>
  <div class="service" style="left:877px"><div class="photo" role="img" aria-label="Crew laying fresh asphalt" style="background:linear-gradient(180deg,#6d8b55 0%,#3a3a3a 45%,#1f1f1f 100%)"></div><div class="bar"></div><p>Bulk Earthworks</p></div>
  <div class="btn" style="left:516px;top:589px;width:172px;height:43px">View More</div>
</section>

<!-- why choose us -->
<h2 class="section-title" style="top:2298px;color:var(--ink)">Why Choose Us</h2>
<div class="underline" style="top:2365px"></div>

<div class="why-card" style="left:87px;top:2392px">
  <div class="icon"><svg width="36" height="36" viewBox="0 0 36 36" fill="none" stroke="#f5c400" stroke-width="1.6"><rect x="6" y="8" width="14" height="20"/><rect x="16" y="14" width="14" height="14"/><line x1="10" y1="14" x2="16" y2="14"/><line x1="10" y1="19" x2="14" y2="19"/></svg></div>
  <h3>Integrity</h3><p>Lorem Ipsum is simply dummy text of the printing industry.</p>
</div>
<div class="why-card featured" style="left:437px;top:2392px">
  <div class="icon"><svg width="36" height="36" viewBox="0 0 36 36" fill="none" stroke="#fff" stroke-width="1.6"><rect x="8" y="6" width="16" height="22"/><rect x="13" y="10" width="16" height="22" /><line x1="17" y1="17" x2="25" y2="17"/><line x1="17" y1="22" x2="25" y2="22"/></svg></div>
  <h3>Accountability</h3><p>Lorem Ipsum is simply dummy text of the printing industry.</p>
</div>
<div class="why-card" style="left:789px;top:2392px">
  <div class="icon"><svg width="36" height="36" viewBox="0 0 36 36" fill="none" stroke="#f5c400" stroke-width="1.6"><path d="M6 20l8-8h8l8 8-12 10z"/><path d="M12 20l6 4 6-4"/></svg></div>
  <h3>Reliability</h3><p>Lorem Ipsum is simply dummy text of the printing industry.</p>
</div>
<div class="why-card" style="left:87px;top:2692px">
  <div class="icon"><svg width="36" height="36" viewBox="0 0 36 36" fill="none" stroke="#f5c400" stroke-width="1.6"><circle cx="18" cy="18" r="5"/><path d="M18 4v6M18 26v6M4 18h6M26 18h6M8 8l4 4M24 24l4 4M28 8l-4 4M12 24l-4 4"/></svg></div>
  <h3>Capability</h3><p>Lorem Ipsum is simply dummy text of the printing industry.</p>
</div>
<div class="why-card" style="left:437px;top:2692px">
  <div class="icon"><svg width="36" height="36" viewBox="0 0 36 36" fill="none" stroke="#f5c400" stroke-width="1.6"><circle cx="18" cy="18" r="11"/><circle cx="18" cy="18" r="4"/><path d="M18 4v4M18 28v4M4 18h4M28 18h4"/></svg></div>
  <h3>Adaptability</h3><p>Lorem Ipsum is simply dummy text of the printing industry.</p>
</div>
<div class="why-card" style="left:789px;top:2692px">
  <div class="icon"><svg width="36" height="36" viewBox="0 0 36 36" fill="none" stroke="#f5c400" stroke-width="1.6"><circle cx="18" cy="18" r="4"/><circle cx="8" cy="10" r="3"/><circle cx="28" cy="10" r="3"/><circle cx="8" cy="27" r="3"/><circle cx="28" cy="27" r="3"/><path d="M10 12l5 4M26 12l-5 4M10 25l5-4M26 25l-5-4"/></svg></div>
  <h3>Ethics</h3><p>Lorem Ipsum is simply dummy text of the printing industry.</p>
</div>

<!-- video -->
<div class="abs video-band"></div>
<h2 class="section-title" style="top:3130px;color:#fff">Watch Our Video</h2>
<p class="section-sub" style="top:3218px;color:#ccc">Lorem Ipsum is simply dummy text of the printing and typesetting industry.</p>
<div class="abs video" role="img" aria-label="Tipper truck and yellow paving machine at a road site"></div>
<svg class="abs" style="left:560px;top:3441px" width="80" height="80" viewBox="0 0 80 80"><circle cx="40" cy="40" r="36" fill="none" stroke="#fff" stroke-width="3"/><path d="M32 26l22 14-22 14z" fill="#fff"/></svg>
<div class="abs video-caption"><b>LOREM IPSUM DUMMY TEXT</b><span>It is a long established fact that a reader will be distracted</span></div>

<!-- contact -->
<div class="abs map" role="img" aria-label="Faint dotted world map background"></div>
<h2 class="section-title" style="top:3770px;color:var(--ink)">Contact Us</h2>
<div class="field" style="left:262px;top:3863px;width:324px;height:47px">
  <svg width="14" height="14" viewBox="0 0 14 14" fill="none" stroke="#f5c400" stroke-width="1.3"><circle cx="7" cy="4.5" r="3"/><path d="M1.5 13c1-3 3-4.5 5.5-4.5s4.5 1.5 5.5 4.5"/></svg>Name</div>
<div class="field" style="left:612px;top:3863px;width:326px;height:47px">
  <svg width="10" height="14" viewBox="0 0 10 14" fill="none" stroke="#f5c400" stroke-width="1.3"><rect x="1" y="0.7" width="8" height="12.6" rx="1.5"/></svg>Phone</div>
<div class="field" style="left:262px;top:3933px;width:676px;height:46px">
  <svg width="15" height="12" viewBox="0 0 15 12" fill="none" stroke="#f5c400" stroke-width="1.3"><rect x="0.7" y="0.7" width="13.6" height="10.6"/><path d="M1 1l6.5 5.5L14 1"/></svg>Email</div>
<div class="field" style="left:262px;top:4003px;width:676px;height:87px">
  <svg width="14" height="14" viewBox="0 0 14 14" fill="none" stroke="#f5c400" stroke-width="1.3"><circle cx="7" cy="7" r="6"/><path d="M4 7h6"/></svg>Message</div>
<div class="btn" style="left:518px;top:4116px;width:170px;height:38px">Submit</div>

<!-- footer -->
<footer class="abs footer">
  <div class="abs brand" style="left:87px"><span class="dot"></span>KESTREL</div>
  <div class="abs footer-links"><span>Home</span><span>Company Overview</span><span>Services</span><span>Personnel</span><span>Experience Record</span><span>Contact Us</span></div>
  <div class="abs copy">© 2019. All Rights Reserved</div>
</footer>

</body>
</html>
```